依頼詳細
企業理念は「ありがとう主義」 赤色が会社のイメージカラーとなります。
「オフィス移転」「内装」を連想させるオリジナリティのある年賀状にしたく、
デザインを募集致します。
今年は対面でご挨拶できない方も多いので、少し目を引く年賀状がいいと思っております。

◆要件
・干支を入れる
・「移転」「引越」「内装工事」「内装デザイン」を連想させる何かを入れる
順位:内装工事>内装デザイン>移転>引越

他:昨年採用をさせて頂いたデザインも添付しますが、
イメージを合わせて頂く必要は御座いません。

参考:https://www.brindlecraft.co.jp/
記載項目
裏面:一般建設業(内装仕上げ工事)東京都都知事許可(般-2)第586207号
社名、代表取締役杉浦健二/社員一同
住所、電話番号、ファックス番号
https://www.brindlecraft.co.jp https://www.kumo-hall527.com/
希望イメージ
シンプル 複雑
単色 カラフル
暗い 明るい
日常 高級
遊び心 厳粛
未来的 伝統的
女性的 男性的
納品ファイル
• 高解像度JPG (.jpg)
• イラストレーター形式 (.ai)
補足説明
デザインの依頼をする機会が少ない為、不足事項等ありましたらご連絡ください。
■ 選んだ理由

社内で選考した結果こちらになりました。
ありがとうございました。

■ 提案者全員のお礼・コメント

この度は弊社の年賀状作成にご協力いただき誠にありがとうございました。
他にも気になるのはありましたので、またご縁がありましたら宜しくお願い致します。

```html
<!DOCTYPE html>
<html lang="ja">
<head>
<meta charset="utf-8">
<title>謹賀新年 2021</title>
<link rel="stylesheet" href="https://fonts.googleapis.com/css2?family=Shippori+Mincho+B1:wght@800&family=Noto+Serif+JP:wght@500;700;900&display=swap">
<style>
  :root {
    --red: #e0201b;
    --red-deep: #c8140f;
    --white: #ffffff;
    --ink: #2a2424;
    --pink: #f6c6c2;
    --city-light: #e9e9eb;
    --city-dark: #a9a9ae;
  }
  html, body { margin: 0; padding: 0; overflow: hidden; background: var(--white); }
  .card {
    position: relative;
    width: 810px; height: 1200px;
    overflow: hidden;
    background: var(--white);
    font-family: "Noto Serif JP", serif;
  }
  .card__shapes { position: absolute; inset: 0; }
  .headline {
    position: absolute; left: 44px; top: 14px; margin: 0;
    font-family: "Shippori Mincho B1", serif;
    font-weight: 800; font-size: 104px; letter-spacing: 2px;
    color: var(--red); line-height: 1.1;
  }
  .date {
    position: absolute; left: 575px; top: 46px;
    font-family: "Shippori Mincho B1", serif; font-weight: 800;
    color: var(--red); font-size: 28px; line-height: 1.15;
  }
  .date span { display: block; }
  .date .date__day { padding-left: 14px; }
  .mascot {
    position: absolute; left: 450px; top: 175px; width: 310px; height: 420px;
    border-radius: 46% 46% 30% 30%;
    background: radial-gradient(ellipse at 50% 35%, #ffffff 0%, #f2f0ee 45%, #d9d5d2 100%);
  }
  .tagline {
    position: absolute; left: 100px; top: 372px;
    transform: rotate(-10deg); transform-origin: left top;
    color: var(--red); font-weight: 700; font-size: 20px; line-height: 1.25;
    background: var(--white);
    padding: 4px 8px;
  }
  .greeting {
    position: absolute; left: 108px; top: 418px; margin: 0;
    color: var(--white); font-weight: 700; font-size: 30px; line-height: 1.55;
    letter-spacing: 1px;
  }
  .company {
    position: absolute; left: 0; right: 0; top: 650px;
    text-align: center; color: var(--ink);
    font-weight: 500; font-size: 17px; line-height: 1.6;
  }
  .company p { margin: 0; }
  .company .company__name { font-size: 20px; font-weight: 700; }
  .slogan {
    position: absolute; left: 0; right: 0; bottom: -28px;
    text-align: center; margin: 0;
    font-family: "Shippori Mincho B1", serif; font-weight: 800;
    font-size: 176px; letter-spacing: 6px;
    color: transparent; -webkit-text-stroke: 3px var(--pink);
  }
</style>
</head>
<body>
<main class="card">
  <svg class="card__shapes" width="810" height="1200" viewBox="0 0 810 1200">
    <defs>
      <linearGradient id="city" x1="0" y1="0" x2="0" y2="1">
        <stop offset="0" stop-color="#e9e9eb"/>
        <stop offset="1" stop-color="#a9a9ae"/>
      </linearGradient>
    </defs>
    <rect role="img" aria-label="オフィスビル街の写真" x="300" y="120" width="510" height="320" fill="url(#city)"/>
    <polygon class="paint-band" points="0,250 810,340 810,610 0,635" fill="#e0201b"/>
    <polygon class="paint-band paint-band--base" points="0,830 810,880 810,1200 0,1200" fill="#c8140f"/>
  </svg>

  <h1 class="headline">謹賀新年</h1>
  <div class="date"><span>令和三年</span><span class="date__day">元旦</span></div>

  <div class="mascot" role="img" aria-label="ペンキローラーで赤く塗りながら走る丑年の牛のキャラクター"></div>
  <div class="tagline">『ありがとう』と共に、<br>今年も走り抜けます!</div>

  <p class="greeting">本年も皆様のお役に<br>立てるよう、一層の<br>努力を持ってご温情に<br>お応えしてまいります。</p>

  <section class="company">
    <p>一般建設業(内装仕上げ工事)東京都都知事許可(般-2)第586207号</p>
    <p class="company__name">株式会社ブリンドルクラフト　代表取締役杉浦健二/社員一同</p>
    <p>〒160-0023 東京都新宿区西新宿3-8-1 西新宿青葉ビル7階</p>
    <p>TEL:03-4580-2716(代)　FAX:03-4580-2717</p>
    <p>https://www.brindlecraft.co.jp　https://www.kumo-hall527.com/</p>
  </section>

  <p class="slogan">IT×内装</p>
</main>
</body>
</html>
```